Sales Process Flyer

Attached is a sketch (2 pages) Id like to have a 1 page "flyer" that will explain the sales strategy for a new recruit.
Ill need to edit this down the road, so if you do it in Illustrator we will be able to handle that.
If you plenvo sales funnel you will see what im going for with the bad funnel drawing.
Id like to have icons with the text thats on the 2nd page (although it would all be 1 page)
Our brand guidelines are attached with some example pieces we have done in the past
Would like this to have an infographic type look

Something I didnt work in the sketch is below.
Estimated Sales Time:
25% - Meeting & Managing Existing Clients
25% - Free Assessments & Proposals
25% - Cold Calling
25% - New Customer Meetings & Networking

Plenvo

```html
<!DOCTYPE html>
<html lang="en">
<head>
<meta charset="utf-8">
<title>Sales Strategy Flyer</title>
<link rel="stylesheet" href="https://fonts.googleapis.com/css2?family=Bebas+Neue&family=Barlow:wght@300;400;600;700;900&display=swap">
<style>
  :root {
    --slate: #33434c;
    --slate-dark: #2c3a42;
    --ink: #2e2e30;
    --grey-text: #6a6a6c;
    --bg-light: #f2f2f3;
    --bg-mid: #d9d9dc;
    --chevron-dark: #333536;
    --chevron-grey: #7b8083;
    --teal: #1e6f90;
    --funnel-blue: #3f74ad;
    --funnel-deep: #2a5584;
    --funnel-light: #f4f7fb;
    --stream: #bcd9ef;
    --white: #ffffff;
    --logo-circle: #58585a;
  }
  html, body { margin: 0; padding: 0; }
  body { width: 927px; height: 1200px; overflow: hidden; background: var(--bg-light); }
  .canvas { position: relative; width: 927px; height: 1200px; overflow: hidden; }
  .art {
    position: absolute; left: 0; top: 0; width: 900px; height: 1165px;
    transform: scale(1.03); transform-origin: 0 0;
    background: radial-gradient(ellipse at 45% 40%, var(--white) 0%, var(--bg-light) 45%, var(--bg-mid) 100%);
    font-family: "Barlow", Arial, sans-serif; color: var(--ink);
    overflow: hidden;
  }
  .backdrop { position: absolute; left: 0; top: 0; width: 900px; height: 1165px; }

  .brand { position: absolute; left: 20px; top: 45px; width: 260px; text-align: center; }
  .brand-mark { width: 164px; height: 164px; border-radius: 50%; background: var(--logo-circle); margin: 0 auto 8px 46px; }
  .brand-name { font-weight: 300; font-size: 37px; line-height: 36px; color: var(--grey-text); margin-left: -10px; }

  .title { position: absolute; left: 288px; top: 18px; margin: 0; white-space: nowrap;
    font-family: "Bebas Neue", "Oswald", sans-serif; font-weight: 400; font-size: 140px; line-height: 140px;
    letter-spacing: 0; color: var(--slate);
    transform: scaleX(0.735); transform-origin: 0 0; }
  .tagline { position: absolute; left: 292px; top: 150px; width: 540px; display: flex; align-items: center; gap: 12px;
    font-size: 33px; line-height: 40px; color: var(--ink); white-space: nowrap; }
  .tagline::before, .tagline::after { content: ""; flex: 1; height: 1.5px; background: var(--ink); }

  .activities { position: absolute; left: 25px; top: 352px; width: 350px; font-size: 15px; line-height: 19px; color: #3a3a3c; }
  .activity { margin: 0 0 10px; }
  .activity b { font-weight: 700; color: var(--ink); }
  .activity.with-icon { display: flex; gap: 14px; margin-bottom: 14px; }
  .activity-square { flex: none; width: 28px; height: 28px; background: var(--slate); margin-top: 4px; }
  .activity .indent { padding-left: 75px; }

  .time-title { position: absolute; left: 25px; top: 672px; margin: 0; font-weight: 700; font-size: 19px; letter-spacing: .5px; color: var(--slate-dark); }
  .time-row { position: absolute; left: 25px; display: flex; align-items: center; }
  .time-pct { width: 47px; font-size: 20px; font-weight: 300; color: #444; }
  .chevron { position: relative; width: 312px; height: 32px; line-height: 32px; padding-left: 28px; font-size: 15px; color: var(--white); white-space: nowrap;
    clip-path: polygon(0 0, 94% 0, 100% 50%, 94% 100%, 0 100%); }
  .chevron.dark { background: var(--chevron-dark); }
  .chevron.grey { background: var(--chevron-grey); color: #2a2a2a; }

  .stage { position: absolute; font-size: 17px; line-height: 23px; color: #333; white-space: nowrap; }
  .stage-metric { position: absolute; font-size: 17px; line-height: 23px; color: #333; white-space: nowrap; }
  .won { position: absolute; left: 612px; top: 966px; font-weight: 900; font-size: 36px; line-height: 42px; color: var(--slate-dark); letter-spacing: 1px; }
  .lost { position: absolute; left: 354px; top: 960px; font-size: 17px; line-height: 23px; color: #333; }
</style>
</head>
<body>
<div class="canvas">
  <div class="art">
    <svg class="backdrop" viewBox="0 0 900 1165" aria-hidden="true">
      <defs>
        <linearGradient id="funnelBody" x1="0" x2="1" y1="0" y2="0">
          <stop offset="0" stop-color="var(--funnel-deep)"/>
          <stop offset="0.2" stop-color="var(--funnel-blue)"/>
          <stop offset="0.55" stop-color="var(--funnel-light)"/>
          <stop offset="0.85" stop-color="var(--funnel-blue)"/>
          <stop offset="1" stop-color="var(--funnel-deep)"/>
        </linearGradient>
        <linearGradient id="stripeFade" x1="0" y1="0" x2="0" y2="1">
          <stop offset="0" stop-color="var(--teal)" stop-opacity="0"/>
          <stop offset="0.4" stop-color="var(--teal)" stop-opacity="1"/>
        </linearGradient>
      </defs>

      <path class="funnel-body" d="M280,236 L566,1052 Q690,1066 812,1046 L906,240 Z" fill="url(#funnelBody)"/>
      <g class="funnel-dividers" fill="none" stroke="var(--funnel-deep)" stroke-width="7">
        <path d="M328,373 Q610,400 899,374"/>
        <path d="M373,503 Q630,528 892,505"/>
        <path d="M419,637 Q650,660 883,636"/>
        <path d="M467,774 Q660,796 867,774"/>
        <path d="M514,907 Q680,926 842,905"/>
      </g>
      <path class="funnel-stream" d="M684,255 Q690,640 622,1045" fill="none" stroke="var(--stream)" stroke-width="7"/>
      <ellipse class="funnel-rim" cx="593" cy="240" rx="313" ry="11" fill="var(--funnel-blue)" stroke="var(--funnel-deep)" stroke-width="4"/>

      <path class="wave-grey" d="M0,900 Q150,960 330,1040 Q520,1110 900,1000 L900,1165 L0,1165 Z" fill="#5d6a72"/>
      <path class="wave-white" d="M0,930 Q170,1000 330,1060 Q540,1130 900,1030 L900,1165 L0,1165 Z" fill="var(--white)"/>
      <path class="wave-teal" d="M0,950 Q170,1020 330,1075 Q540,1140 900,1050 L900,1165 L0,1165 Z" fill="var(--teal)"/>
      <path class="wave-dark" d="M0,985 Q180,1055 340,1105 Q560,1160 900,1075 L900,1165 L0,1165 Z" fill="var(--slate)"/>
      <path class="diagonal-stripe" d="M150,870 L172,870 L290,1165 L262,1165 Z" fill="url(#stripeFade)"/>
      <path class="diagonal-white" d="M0,915 L200,1165 L184,1165 L0,935 Z" fill="var(--white)"/>
    </svg>

    <div class="brand">
      <div class="brand-mark"></div>
      <div class="brand-name">Slate Peak<br>Design</div>
    </div>

    <h1 class="title">SALES STRATERGY</h1>
    <div class="tagline">Stratergy • Effort • Skill</div>

    <div class="activities">
      <p class="activity with-icon"><span class="activity-square"></span><span><b>Blogging</b> - 4 post per month<br>on industry specific topic</span></p>
      <p class="activity with-icon"><span class="activity-square"></span><span><b>Linkora</b> - 1 hour per week<br>prospecting and connecting</span></p>
      <p class="activity" style="margin-bottom:20px"><b>Networking</b> - 4 events per month</p>
      <p class="activity" style="margin-bottom:20px"><b>Account management</b> -<br>1 hour per week checking in with previous clients</p>
      <p class="activity" style="margin-bottom:20px"><b>Trade Shows</b> - 1 per month</p>
      <p class="activity"><b>Referrals</b> - Ask for referral , generate 1 referral<br><span class="indent">per week</span></p>
    </div>

    <h2 class="time-title">ESTIMATED SALES TIME:</h2>
    <div class="time-row" style="top:715px"><span class="time-pct">25%</span><span class="chevron dark">Meeting &amp; Managing Existing Clients</span></div>
    <div class="time-row" style="top:757px"><span class="time-pct">25%</span><span class="chevron grey">Free Assessments &amp; Proposals</span></div>
    <div class="time-row" style="top:805px"><span class="time-pct">25%</span><span class="chevron dark">Cold Calling</span></div>
    <div class="time-row" style="top:846px"><span class="time-pct">25%</span><span class="chevron grey">New Customer Meetings &amp; Networking</span></div>

    <div class="stage" style="left:351px;top:282px">Landing page created on website<br>Specific Email Crafted<br>500 Emails sent</div>
    <div class="stage-metric" style="left:711px;top:292px">5% - Email Sent<br>10% first contacts</div>

    <div class="stage" style="left:379px;top:405px">Phone call follow up with clicks<br>Phone call follow up with opens<br>Phone call follow up with removin<br>*Make free assessment pitch</div>
    <div class="stage-metric" style="left:711px;top:429px">180 goal<br>25% assessment</div>

    <div class="stage" style="left:433px;top:570px">Run free assessment</div>
    <div class="stage-metric" style="left:711px;top:570px">60 goal<br>50% meeting</div>

    <div class="stage" style="left:469px;top:703px">Meeting scheduled</div>
    <div class="stage-metric" style="left:699px;top:703px">32 goal<br>75% proposal</div>

    <div class="stage" style="left:518px;top:844px">Proposal</div>
    <div class="stage-metric" style="left:689px;top:844px">16 goal</div>

    <div class="won">WON</div>
    <div class="lost">Lost - Price<br>Lost - Timeline<br>Lost - Unknown</div>
  </div>
</div>
</body>
</html>
```